Vexora Promo Consulting Company Website

Need a website for a consulting company that will help nonprofits qualify to get free online ads from Vexora in their Vexora Promo Bursary program and that will also help them manage the ad spend. Need a new logo as part of this. You can look at our current site at www.lumenhallow.com to get a sense as to content. I am looking for a nice looking site that will be easy to maintain and expand upon. It should load fast and be good design from an SEO perspective.
Updates

Need extra days to review

Target Market(s)

Midsized nonprofits.

Industry/Entity Type

nonprofit marketing

Coding

Coded - Design and coding required

Number of Pages Required

5+ page

```html
<!DOCTYPE html>
<html lang="en">
<head>
<meta charset="utf-8">
<title>Lumen Hallow – Vexora Promo Bursary Consulting</title>
<link href="https://fonts.googleapis.com/css2?family=Lato:wght@400;700;900&family=Oswald:wght@500&display=swap" rel="stylesheet">
<style>
:root{
  --navy:#2a4a9c;
  --navy-deep:#1b2c63;
  --ink:#0e1636;
  --orange:#f5821f;
  --text:#333a4d;
  --mist:#f3eff0;
  --white:#ffffff;
}
*{box-sizing:border-box;margin:0;padding:0}
html,body{width:1200px;height:3708px;overflow:hidden}
body{position:relative;font-family:'Lato',sans-serif;color:var(--text);background:var(--white)}
.abs{position:absolute}
.bar{color:var(--orange);font-weight:400}

/* header */
.site-header{left:0;top:0;width:1200px;height:72px;background:var(--white);z-index:5}
.brand{left:158px;top:18px;font-family:'Oswald',sans-serif;font-weight:500;font-size:31px;color:var(--navy);letter-spacing:.5px}
.nav{right:155px;top:28px;display:flex;gap:24px;font-size:14px;letter-spacing:.3px;color:#2b2f3a}
.nav .active{color:var(--orange)}

/* hero */
.hero-photo{left:0;top:72px;width:1200px;height:650px;background:linear-gradient(160deg,#3d3b43 0%,#1f2030 45%,#2a2b3b 100%)}
.hero-title{left:0;top:162px;width:1200px;text-align:center;color:var(--white);font-weight:900;font-size:35px;line-height:47px;letter-spacing:.3px}
.hero-sub{left:0;top:262px;width:1200px;text-align:center;color:var(--white);font-size:24px;line-height:34px}
.btn{display:inline-block;background:var(--orange);color:var(--white);font-weight:700;font-size:14px;text-align:center;text-transform:uppercase}
.hero-btn{left:515px;top:344px;width:170px;height:37px;line-height:37px}

.feature{width:300px;height:300px;border-radius:50%;border:12px solid var(--orange);background:var(--white);padding:2px}
.feature-inner{width:100%;height:100%;border-radius:50%;background:var(--navy);color:var(--white);text-align:center;padding-top:50px}
.feature.dark .feature-inner{background:var(--navy-deep)}
.feature h3{font-size:17px;font-weight:400;line-height:24px;margin:12px 0 8px;letter-spacing:.3px}
.feature p{font-size:12px;line-height:19px;padding:0 38px}

.section-title{font-weight:900;font-size:27px;color:var(--navy);letter-spacing:.2px}
.intro-title{left:0;top:765px;width:1200px;text-align:center}
.intro-text{left:250px;top:815px;width:700px;text-align:center;font-size:13px;line-height:22px}

/* about */
.about-photo{left:0;top:940px;width:600px;height:433px;background:linear-gradient(135deg,#c9d3e0 0%,#8fa0b8 45%,#e3e7ee 100%)}
.about-panel{left:600px;top:940px;width:600px;height:433px;background:var(--navy);color:var(--white);padding:112px 140px 0 83px}
.about-panel h2{font-size:27px;font-weight:900;margin-bottom:20px}
.about-panel p{font-size:13px;line-height:22px}

/* process */
.process-title{left:0;top:1438px;width:1200px;text-align:center}
.dots{left:158px;top:1551px;width:884px;border-top:2px dotted var(--navy)}
.step-icon{width:46px;height:46px;border-radius:50%;background:var(--orange);border:4px solid #fff;box-shadow:0 0 0 1px #f0d3b8;top:1528px}
.process-cards{left:158px;top:1594px;width:884px;height:375px;display:flex}
.card{flex:1;color:var(--white);text-align:center;padding:56px 16px 0;position:relative}
.card:nth-child(1){background:#2c4690}
.card:nth-child(2){background:#27418a}
.card:nth-child(3){background:#2d4994}
.card:nth-child(4){background:#2f4d9a}
.card::before{content:"";position:absolute;top:-10px;left:50%;margin-left:-11px;border:11px solid transparent;border-top:0;border-bottom:10px solid #243b80}
.card h3{font-size:17px;font-weight:400;line-height:27px;margin-bottom:10px;letter-spacing:.3px}
.card p{font-size:12px;line-height:19.5px}

/* experience */
.exp-title{left:160px;top:2216px;width:500px;font-size:27px;line-height:36px}
.exp-text{left:160px;top:2345px;width:490px;font-size:13px;line-height:22px}
.exp-btn{left:158px;top:2458px;width:170px;height:36px;line-height:36px}
.exp-frame{left:676px;top:2134px;width:366px;height:410px;background:var(--orange);border-radius:60px 0 0 0}
.exp-photo{left:683px;top:2141px;width:359px;height:403px;border-radius:54px 0 0 0;background:linear-gradient(150deg,#7c8a97 0%,#aab4bf 40%,#5b6470 100%)}

/* contact */
.contact-ring{left:160px;top:2665px;width:424px;height:424px;border-radius:50%;border:14px solid var(--orange);border-right-color:transparent;transform:rotate(-20deg)}
.contact-photo{left:190px;top:2688px;width:392px;height:392px;border-radius:50%;background:radial-gradient(circle at 55% 45%,#e9eaee 0%,#b5b8c0 55%,#6c707a 100%)}
.start-title{left:665px;top:2715px}
.field{background:var(--white);border:1px solid #d4d6dc;box-shadow:0 1px 3px rgba(0,0,0,.08);font-size:12px;color:#444;padding:16px 18px 0;letter-spacing:.3px}
.start-btn{left:665px;top:2992px;width:171px;height:37px;line-height:37px}

/* footer */
.footer-brand{left:158px;top:3300px;font-family:'Oswald',sans-serif;font-weight:500;font-size:30px;color:var(--navy)}
.footer-text{left:158px;top:3363px;width:250px;color:var(--white);font-size:13px;line-height:19px}
.phone{left:158px;top:3432px;display:flex;align-items:center;gap:14px;color:var(--white);font-weight:700;font-size:14px}
.phone .ring{width:38px;height:38px;border-radius:50%;border:2px solid var(--orange);display:flex;align-items:center;justify-content:center}
.f-col h4{color:var(--white);font-weight:400;font-size:15px;margin-bottom:24px;letter-spacing:.2px}
.f-col ul{list-style:none;color:var(--white);font-size:13px;line-height:29.5px}
.news-input{left:819px;top:3373px;width:223px;height:37px;background:var(--white);font-size:12px;color:#222;padding:11px 20px}
.news-btn{left:819px;top:3418px;width:223px;height:36px;line-height:36px;font-size:13px}
.rule{top:3543px;height:1px;background:#3a4568}
.socials{left:508px;top:3524px;display:flex;gap:11px}
.socials span{width:38px;height:38px;border-radius:50%;border:2px solid var(--orange);background:var(--ink)}
.copyright{left:0;top:3616px;width:1200px;text-align:center;color:var(--white);font-size:12px}
</style>
</head>
<body>

<header class="site-header abs">
  <div class="brand abs">LUMEN HALLOW</div>
  <nav class="nav abs"><span class="active">HOME</span><span>SERVICES</span><span>INFORMATION CENTER</span><span>CONTACT</span></nav>
</header>

<section class="hero">
  <div class="hero-photo abs" role="img" aria-label="Photo of consultants meeting in an office, darkened"></div>
  <svg class="abs" style="left:0;top:560px" width="1200" height="170" viewBox="0 560 1200 170">
    <path d="M0 636 C300 560 560 600 760 662 C900 705 1060 722 1200 705 L1200 730 L0 730 Z" fill="#fff"/>
    <path d="M700 650 C880 600 1060 590 1200 612 L1200 712 C1060 680 900 660 760 664 Z" fill="var(--orange)"/>
  </svg>
  <h1 class="hero-title abs">VEXORA PROMO BURSARY ACQUISITION<br>TO MANAGEMENT AND REACTIVATION</h1>
  <p class="hero-sub abs">Is Your Nonprofit Organization taking advantage<br>of Vexora Promo Bursaries ?</p>
  <a class="btn hero-btn abs">Learn More</a>

  <div class="feature abs" style="left:156px;top:418px"><div class="feature-inner">
    <svg width="56" height="52" viewBox="0 0 56 52" fill="none" stroke="#fff" stroke-width="2"><circle cx="30" cy="20" r="12"/><path d="M30 13v14M26 17h6a2 2 0 010 4h-4a2 2 0 000 4h6"/><path d="M6 44l10-10h12l8 6-6 4H20M6 44l8 6"/></svg>
    <h3>AFFORDABLE</h3><p>Your success is our bottom line! Low costs, no contracts, and complete transparency.</p></div></div>
  <div class="feature dark abs" style="left:450px;top:418px"><div class="feature-inner">
    <svg width="56" height="52" viewBox="0 0 56 52" fill="none" stroke="#fff" stroke-width="2"><circle cx="28" cy="10" r="6"/><circle cx="16" cy="20" r="6"/><circle cx="40" cy="20" r="6"/><path d="M8 34l10 10h20l10-10M14 30l6 6M42 30l-6 6"/></svg>
    <h3>EXPERIENCE<br>MATTERS</h3><p>With over 30 years of working with nonprofits,You can count on our intimate knowledge.</p></div></div>
  <div class="feature abs" style="left:744px;top:418px"><div class="feature-inner">
    <svg width="56" height="52" viewBox="0 0 56 52" fill="none" stroke="#fff" stroke-width="2"><circle cx="28" cy="20" r="15"/><circle cx="28" cy="20" r="9"/><path d="M28 15l2 4h4l-3 3 1 4-4-2-4 2 1-4-3-3h4z"/><path d="M20 33l-4 15 6-3 4 5 2-12M36 33l4 15-6-3-4 5"/></svg>
    <h3>ACCESSIBILITY</h3><p>You will have complete access to your very own account manager. We make the process seamless.</p></div></div>
</section>

<h2 class="section-title intro-title abs">VEXORA PROMO BURSARIES <span class="bar">|</span> ACQUISITION</h2>
<p class="intro-text abs">The Vexora Promo Bursaries program is a must for all eligible charitable organizations. It is a unique opportunity for organizations to extend their public service messages to a wider audience in an effort to gain new donors, attract volunteers, and further your organization’s impact.</p>

<section>
  <div class="about-photo abs" role="img" aria-label="Photo of a hand with a pen reviewing printed charts beside a phone"></div>
  <div class="about-panel abs">
    <h2>ABOUT <span class="bar">|</span> US</h2>
    <p>Lumen Hallow was formed by nonprofit digital advertising professionals for the sole purpose of helping nonprofit organizations acquire and manage Vexora Promo bursaries. Our experience in the nonprofit sector, coupled with our digital advertising expertise, puts us in a strong position to deliver unmatched Vexora Promo acquisition and management services.</p>
  </div>
</section>

<section>
  <h2 class="section-title process-title abs">OUR <span class="bar">|</span> PROCESS</h2>
  <div class="dots abs"></div>
  <div class="step-icon abs" style="left:249px"><svg width="38" height="38" viewBox="0 0 38 38" fill="none" stroke="#fff" stroke-width="1.8"><rect x="12" y="10" width="14" height="10"/><path d="M9 26h20M13 20v6M25 20v6"/></svg></div>
  <div class="step-icon abs" style="left:472px"><svg width="38" height="38" viewBox="0 0 38 38" fill="none" stroke="#fff" stroke-width="1.8"><rect x="10" y="11" width="18" height="16" rx="1"/><path d="M10 15h18M14 19h10M14 23h6"/></svg></div>
  <div class="step-icon abs" style="left:689px"><svg width="38" height="38" viewBox="0 0 38 38" fill="none" stroke="#fff" stroke-width="1.8"><path d="M19 9l9 4v6c0 5-4 9-9 10-5-1-9-5-9-10v-6z"/><circle cx="19" cy="18" r="3"/></svg></div>
  <div class="step-icon abs" style="left:909px"><svg width="38" height="38" viewBox="0 0 38 38" fill="none" stroke="#fff" stroke-width="1.8"><rect x="10" y="11" width="18" height="16"/><path d="M10 16h18M20 16v11M13 20h4M13 23h4"/></svg></div>

  <div class="process-cards abs" role="list">
    <div class="card" role="listitem"><h3>INITIAL<br>CONSULTATION</h3><p>Our Vexora Promo Bursaries are industry specialists. We work with every type of nonprofit organization, large and small on a daily basis. Our experience in the nonprofit sector sets us up to hit the ground running on your behalf.</p></div>
    <div class="card" role="listitem"><h3>WEBSITE<br>READINESS</h3><p>One of Vexora’s eligibility requirements is to have a website the meets certain criteria. Our experienced developers will make sure that your website is up to standard. If there are any issues, we will resolve them in consultation with you.</p></div>
    <div class="card" role="listitem"><h3>GRANT<br>ACQUISITION</h3><p>Sit back and leave your Vexora grants acquisition to us. If we need any documentation from you during the acquisition process, your Lumen Hallow account manager will reach out to you.</p></div>
    <div class="card" role="listitem"><h3>VEXORA<br>PROMO SETUP</h3><p>If you do not have one already, our Vexora Promo specialists will help set up your Vexora account. Once set up,</p>
      <svg width="20" height="20" viewBox="0 0 20 20" style="margin-top:12px" fill="none" stroke="#fff" stroke-width="1.3"><circle cx="10" cy="10" r="8"/><path d="M10 6v8M6 10h8"/></svg></div>
  </div>
</section>

<section>
  <svg class="abs" style="left:0;top:1990px" width="1200" height="610" viewBox="0 0 1200 610">
    <path d="M0 0 C120 110 260 130 520 118 C760 108 980 50 1200 0 L1200 607 L0 607 Z" fill="var(--mist)"/>
  </svg>
  <h2 class="section-title exp-title abs">WE HAVE WORKED WITH NONPROFIT ORGANIZATIONS LARGE AND SMALL FOR OVER 30 YEARS.</h2>
  <p class="exp-text abs">From formation, management, compliance, fundraising, etc. we have unmatched experience in the nonprofit sector. We are proud to have nonprofit fundraisers and current nonprofit volunteers in our team of nonprofit Vexora grants management team</p>
  <a class="btn exp-btn abs">Contact Us Now</a>
  <div class="exp-frame abs"></div>
  <div class="exp-photo abs" role="img" aria-label="Photo of a laptop showing a charity donation page"></div>
</section>

<section>
  <div class="contact-ring abs"></div>
  <div class="contact-photo abs" role="img" aria-label="Photo of a hand holding a phone over a keyboard"></div>
  <h2 class="section-title start-title abs">GET <span class="bar">|</span> STARTED</h2>
  <div class="field abs" style="left:665px;top:2763px;width:184px;height:43px">FIRST NAME :</div>
  <div class="field abs" style="left:856px;top:2763px;width:185px;height:38px">LAST NAME :</div>
  <div class="field abs" style="left:665px;top:2823px;width:184px;height:41px">EMAIL :</div>
  <div class="field abs" style="left:856px;top:2816px;width:185px;height:38px">PHONE NO :</div>
  <div class="field abs" style="left:665px;top:2879px;width:376px;height:100px">MESSAGE :</div>
  <a class="btn start-btn abs">Contact Us Now</a>
</section>

<footer>
  <svg class="abs" style="left:0;top:3040px" width="1200" height="668" viewBox="0 0 1200 668">
    <path d="M0 20 C260 150 520 160 760 118 C960 82 1080 40 1200 0 L1200 668 L0 668 Z" fill="var(--ink)"/>
  </svg>
  <div class="footer-brand abs">LUMEN HALLOW</div>
  <p class="footer-text abs">From Vexora Promo Bursary acquisition to management, and reactivation, we have you covered!</p>
  <div class="phone abs"><span class="ring"><svg width="18" height="18" viewBox="0 0 24 24" fill="var(--orange)"><path d="M6.6 10.8a15 15 0 006.6 6.6l2.2-2.2c.3-.3.7-.4 1-.2 1.1.4 2.3.6 3.6.6.6 0 1 .4 1 1V20c0 .6-.4 1-1 1A17 17 0 013 4c0-.6.4-1 1-1h3.5c.6 0 1 .4 1 1 0 1.3.2 2.5.6 3.6.1.3 0 .7-.2 1z"/></svg></span>TEL : 555-014-2738</div>
  <div class="f-col abs" style="left:451px;top:3313px"><h4>QUICK<span class="bar">|</span>LINK</h4><ul><li>Home</li><li>Services</li><li>Information Center</li><li>Contact</li></ul></div>
  <div class="f-col abs" style="left:637px;top:3313px"><h4>OUR<span class="bar">|</span>SERVICES</h4><ul><li>Initial Consultation</li><li>Website Readiness</li><li>Grant Acquisition</li><li>Vexora Promo Setup</li></ul></div>
  <div class="f-col abs" style="left:816px;top:3313px"><h4>SIGN UP <span class="bar">|</span> TO NEWSLETTER</h4></div>
  <div class="news-input abs">Enter Your Mail ID</div>
  <a class="btn news-btn abs">Subscribe Now</a>
  <div class="rule abs" style="left:158px;width:340px"></div>
  <div class="rule abs" style="left:702px;width:340px"></div>
  <div class="socials abs" aria-label="Social links"><span></span><span></span><span></span><span></span></div>
  <p class="copyright abs">Copyright©2021 <strong>Lumen Hallow</strong> All Rights Reserved.</p>
</footer>

</body>
</html>
```